New Website for IT Services Business

We need an uncoded web design for a new company based in Australia called "Falcon Tech". We offer specialised point of sale (POS) support to the hospitality industry. We already support hundreds of cafes and restaurants. We are also about to launch and promote a range of new services with the offering of General IT Support being the most important. Other additional services to be offered are Falcon Cloud Backup, reselling and supporting Korvel Antivirus and Tresby Apps.

We have a logo design and our colour scheme is based on the logo with the addition of charcoal grey (see attached logos). We want the pages to reflect precision and efficiency with sharp characteristics. It must be professional but playful/fun elements are encouraged.

Our target audience is restaurant and cafe owners who are interested in finding high quality POS and IT support for their business.

The main call to action on the home page should be either 'Let's Meet For Coffee!' or 'Find out more (by completing a form)'. If you are unsure about what the general text should say then you can use 'Lorem Ipsum' where required.

The site must be viewable at different resolutions and on smart phones and tablets.

The website structure will be quite simple. We require:
- one impressive landing page. Visitors will quickly determine our services and that we provide a very high level of service while also offering value for money. Obviously a clear list of links (however/wherever you like) to the other pages.
- Simple pages with a similar layout for the following:
- Services - "POS & IT Support for the Hospitality Industry" being the main one. With complementary services also listed. Another call to action on this page with the option of 'Let's Meet For Coffee' or a "More information/Pricing" form to be completed by the visitor.
- Products - will be a small online storefront for a few simple products.
- About - Business background. 2x Directors with a photo and brief Bio.
- Downloads - A list of free files to download. Includes remote access client software.
- Contact Us - Mailing address, Email addresses and Support phone number.

Please feel free to ask any questions about the design. I will assist as much as possible.

Thank you for viewing. We promise to give constructive feedback to every person who submits a design. Thank you so much.

Target Market(s)

Restaurant and Cafe owners.

Industry/Entity Type

Hospitality

Requirements
Must have
• - Viewable on different resolutions and on smart phones and tablets.
- Clear call to action of EITHER 'Let's Meet For Coffee' or a "More information/Pricing" form to be completed by the visitor.

```html
<!DOCTYPE html>
<html lang="en">
<head>
<meta charset="utf-8">
<title>Falcon Tech – POS &amp; IT Support for Hospitality</title>
<link href="https://fonts.googleapis.com/css2?family=Oswald:wght@500;700&family=Open+Sans:ital,wght@0,400;0,600;0,700;1,400&family=PT+Serif&family=Shadows+Into+Light&display=swap" rel="stylesheet">
<style>
  :root{
    --red:#c8101a;
    --red-dark:#9e0b12;
    --charcoal:#2b2b2b;
    --charcoal-deep:#1f1f1f;
    --cyan:#29b6e8;
    --cyan-light:#5fd0f5;
    --grey-page:#e6e6e6;
    --grey-panel:#ffffff;
    --grey-circle:#d9d9d9;
    --text:#3a3a3a;
    --text-muted:#666;
    --white:#fff;
  }
  *{box-sizing:border-box;margin:0;padding:0}
  html,body{width:779px;height:1200px;overflow:hidden}
  body{position:relative;background:repeating-linear-gradient(90deg,#e9e9e9 0 3px,#e2e2e2 3px 6px);font-family:"Open Sans",sans-serif;color:var(--text)}

  /* header */
  .site-header{position:absolute;left:0;top:0;width:779px;height:47px;background:linear-gradient(#fafafa,#ececec);border-bottom:1px solid #d4d4d4;z-index:3}
  .brand{position:absolute;left:76px;top:0;width:141px;height:78px;background:var(--white);box-shadow:0 2px 6px rgba(0,0,0,.25);transform:skewY(-4deg);transform-origin:left top;z-index:4;display:flex;align-items:center;justify-content:center;gap:6px}
  .brand-mark{width:20px;height:20px;border-radius:50%;background:var(--red);transform:skewY(4deg)}
  .brand-name{font-family:"Open Sans",sans-serif;font-weight:700;font-size:17px;color:var(--red);transform:skewY(4deg)}
  .main-nav a{position:absolute;top:13px;font-family:"Oswald",sans-serif;font-weight:500;font-size:12.5px;line-height:18px;color:var(--charcoal);text-decoration:none;z-index:5}
  .main-nav a.is-active{background:var(--red);color:var(--white);transform:skewX(-12deg);padding:0 6px;margin-left:-6px}
  .main-nav a.is-active span{display:inline-block;transform:skewX(12deg)}
  .social{position:absolute;left:651px;top:15px;display:flex;gap:3px;z-index:5}
  .social i{display:block;width:16px;height:16px;border-radius:50%;background:#2e7fbf}

  /* hero */
  .hero{position:absolute;left:0;top:47px;width:779px;height:304px;background:radial-gradient(ellipse at 40% 30%,#9fb3c3 0%,#6b7a86 45%,#2d3238 100%)}
  .hero-arrow{position:absolute;top:165px}
  .hero-band{position:absolute;left:102px;top:175px;width:574px;height:53px;background:rgba(200,16,26,.82);transform:skewX(-10deg)}
  .hero-title{position:absolute;left:131px;top:177px;font-family:"Oswald",sans-serif;font-weight:700;font-size:27px;color:var(--white);letter-spacing:-.3px;line-height:32px}
  .hero-sub{position:absolute;left:534px;top:207px;font-family:"Oswald",sans-serif;font-weight:500;font-size:13px;color:var(--white)}
  .hero-copy{position:absolute;left:129px;top:237px;width:530px;font-size:10.5px;line-height:14px;color:var(--white)}
  .hero-thumbs{position:absolute;left:129px;top:291px;display:flex;gap:2px}
  .hero-thumbs span{width:26px;height:18px;background:linear-gradient(#aeb4ba,#6f767d)}
  .btn-coffee{position:absolute;left:512px;top:285px;width:154px;height:39px;background:linear-gradient(var(--cyan-light),var(--cyan));transform:skewX(-8deg);display:flex;align-items:center;justify-content:center;font-family:"Oswald",sans-serif;font-weight:500;font-size:11.5px;color:var(--white);box-shadow:0 2px 3px rgba(0,0,0,.3)}

  /* content panel */
  .panel{position:absolute;left:76px;top:351px;width:625px;height:710px;background:var(--grey-panel);box-shadow:0 0 6px rgba(0,0,0,.12)}
  .ribbon{position:absolute;left:259px;top:351px;width:262px;height:44px}
  .ribbon-label{position:absolute;left:259px;top:361px;width:262px;text-align:center;font-family:"Oswald",sans-serif;font-weight:500;font-size:16px;color:var(--white)}

  .feature{position:absolute;top:411px;width:160px;text-align:center}
  .feature-circle{width:160px;height:160px;border-radius:50%;background:radial-gradient(circle at 50% 30%,#ededed,var(--grey-circle));display:flex;flex-direction:column;align-items:center;justify-content:center;gap:6px;font-family:"Open Sans",sans-serif;font-weight:700;font-size:14.5px;line-height:15px;color:#555;letter-spacing:-.3px}
  .feature-circle.is-dark{background:radial-gradient(circle at 50% 30%,#4a4a4a,#1e1e1e);color:var(--white);box-shadow:0 0 0 6px #fff,0 0 0 7px #dcdcdc}
  .feature-text{margin:10px auto 0;width:150px;font-size:8.3px;line-height:11px;color:var(--text-muted)}
  .btn-more{display:inline-block;margin-top:8px;width:61px;height:14px;line-height:14px;background:linear-gradient(var(--cyan-light),var(--cyan));transform:skewX(-8deg);font-size:6.5px;color:var(--white)}

  .divider{position:absolute;left:76px;width:625px;height:1px;background:#e3e3e3}

  .general-title{position:absolute;left:102px;top:694px;font-family:"Oswald",sans-serif;font-weight:700;font-size:31px;line-height:33px;color:#444;letter-spacing:-.5px}
  .general-copy{position:absolute;left:102px;top:767px;width:310px;font-size:8.9px;line-height:12.5px;color:var(--text)}
  .general-photo{position:absolute;left:429px;top:690px;width:250px;height:114px;background:linear-gradient(135deg,#c9b79a,#8d8a82 55%,#4c4f55);clip-path:polygon(3% 0,100% 4%,98% 100%,0 96%)}
  .btn-coffee-small{position:absolute;left:417px;top:785px;width:106px;height:28px;background:var(--red);transform:skewX(-6deg);display:flex;align-items:center;justify-content:center;font-family:"Oswald",sans-serif;font-weight:500;font-size:8.5px;color:var(--white)}

  .tab{position:absolute;left:247px;top:857px;width:267px;height:37px;background:#e4e4e4;clip-path:polygon(4% 0,96% 0,100% 100%,0 100%);display:flex;align-items:center;justify-content:center;font-weight:600;font-size:16px;color:#444}
  .service-btn{position:absolute;left:100px;display:flex;align-items:center;gap:7px;padding-left:10px;font-family:"Open Sans",sans-serif;font-weight:700;font-size:11.5px;color:var(--white);background:linear-gradient(#5a5a5a,#3a3a3a);box-shadow:0 2px 3px rgba(0,0,0,.3)}
  .service-btn.is-active{background:var(--red);clip-path:polygon(0 0,87% 0,100% 50%,87% 100%,0 100%);line-height:12px;box-shadow:none}
  .service-copy{position:absolute;left:321px;top:918px;width:352px;font-family:"PT Serif",serif;font-size:9.7px;line-height:13.4px;color:var(--text)}
  .service-more{position:absolute;left:323px;top:996px}

  /* footer */
  .site-footer{position:absolute;left:0;top:1061px;width:779px;height:139px;background:var(--charcoal-deep)}
  .footer-links{position:absolute;top:1089px;font-size:7.8px;line-height:9.5px;color:#ddd}
  .call-label{position:absolute;left:245px;top:1076px;font-family:"Shadows Into Light",cursive;font-size:10px;color:var(--white)}
  .call-number{position:absolute;left:230px;top:1092px;font-family:"Shadows Into Light",cursive;font-size:24px;color:#e0282f;letter-spacing:1px}
  .footer-note{position:absolute;left:463px;top:1091px;font-size:8.7px;line-height:11.5px;font-style:italic;color:var(--white)}
  .footer-note a{color:var(--cyan)}
  .footer-rule{position:absolute;left:76px;top:1133px;width:625px;height:1px;background:#333}
  .legal{position:absolute;left:0;width:779px;text-align:center;font-size:7.8px;color:#999}
</style>
</head>
<body>

<header class="site-header">
  <nav class="main-nav">
    <a href="#" style="left:287px">Home</a>
    <a href="#" class="is-active" style="left:334px"><span>About</span></a>
    <a href="#" style="left:386px">Services</a>
    <a href="#" style="left:451px">Products</a>
    <a href="#" style="left:516px">Downloads</a>
    <a href="#" style="left:592px">Contact</a>
  </nav>
  <div class="social"><i></i><i></i><i></i></div>
</header>
<div class="brand"><span class="brand-mark"></span><span class="brand-name">Falcon Tech</span></div>

<section class="hero" role="img" aria-label="Photo of three smiling business people shaking hands over coffee in an office"></section>
<svg class="hero-arrow" style="left:40px" width="20" height="40" viewBox="0 0 20 40"><polyline points="16,2 4,20 16,38" fill="none" stroke="rgba(255,255,255,.7)" stroke-width="2"/></svg>
<svg class="hero-arrow" style="left:716px" width="20" height="40" viewBox="0 0 20 40"><polyline points="4,2 16,20 4,38" fill="none" stroke="rgba(255,255,255,.7)" stroke-width="2"/></svg>
<div class="hero-band"></div>
<h1 class="hero-title">We Offer Specialized Point of Sale Support to the</h1>
<div class="hero-sub">Hospitality Industry</div>
<p class="hero-copy">We Support Hundreds of Cafes and Restaurants. Lorem Ipsum is simply dummy text of the printing and typesetting industry. Lorem Ipsum has been the industry standard dummy text ever since when an unknown printer took a galley of type and scrambled it to make a type specimen book.</p>
<div class="hero-thumbs" role="img" aria-label="Slide thumbnails"><span></span><span></span><span></span><span></span></div>
<a class="btn-coffee">LET'S MEET FOR COFFEE</a>

<main class="panel"></main>

<svg class="ribbon" viewBox="0 0 262 44"><polygon points="0,0 262,0 252,32 140,32 131,44 122,32 10,32" fill="var(--red)"/></svg>
<div class="ribbon-label">Falcon's Featured Services</div>

<div class="feature" style="left:129px">
  <div class="feature-circle">
    <svg width="20" height="28" viewBox="0 0 20 28"><rect x="2" y="1" width="16" height="26" rx="2" fill="#555"/><rect x="5" y="4" width="10" height="7" fill="#ddd"/><g fill="#ddd"><rect x="5" y="14" width="3" height="2"/><rect x="9" y="14" width="3" height="2"/><rect x="13" y="14" width="2" height="2"/><rect x="5" y="18" width="3" height="2"/><rect x="9" y="18" width="3" height="2"/><rect x="13" y="18" width="2" height="2"/></g></svg>
    <span>POS &amp;<br>IT Support</span>
  </div>
  <p class="feature-text">Lorem Ipsum is simply dummy text the printing galley of type and scrambled it to make a type</p>
  <span class="btn-more">Learn More</span>
</div>
<div class="feature" style="left:312px">
  <div class="feature-circle is-dark">
    <svg width="36" height="32" viewBox="0 0 36 32"><path d="M2 2h32v22H16l-6 6v-6H2z" fill="#fff"/><text x="18" y="19" text-anchor="middle" font-family="Open Sans,sans-serif" font-weight="700" font-size="15" fill="#222">$</text></svg>
    <span>Offering Value<br>for Money</span>
  </div>
  <p class="feature-text">Lorem Ipsum is simply dummy text the printing galley of type and scrambled it to make a type</p>
  <span class="btn-more">Learn More</span>
</div>
<div class="feature" style="left:489px">
  <div class="feature-circle">
    <svg width="32" height="32" viewBox="0 0 32 32"><circle cx="16" cy="16" r="15" fill="#555"/></svg>
    <span>POS &amp;<br>IT Support</span>
  </div>
  <p class="feature-text">Lorem Ipsum is simply dummy text the printing galley of type and scrambled it to make a type</p>
  <span class="btn-more">Learn More</span>
</div>

<div class="divider" style="top:657px"></div>

<h2 class="general-title">Offering of General<br>IT Support</h2>
<p class="general-copy">But I must explain to you how all this mistaken idea of denouncing pleasure and praising pain was born and I will give you a complete account of the system, and expound the actual teachings of the great explorer</p>
<div class="general-photo" role="img" aria-label="Photo of two businessmen talking at a cafe table"></div>
<a class="btn-coffee-small">LET'S MEET FOR COFFEE</a>

<div class="divider" style="top:894px"></div>
<div class="tab">Additional Services</div>

<a class="service-btn" style="top:919px;width:165px;height:27px"><svg width="12" height="9" viewBox="0 0 12 9"><path d="M1 8 Q2 3 8 3 V0 L12 4 L8 8 V5 Q4 5 1 8z" fill="#fff"/></svg>Falcon Cloud Backup</a>
<a class="service-btn is-active" style="top:946px;width:209px;height:45px"><svg width="12" height="9" viewBox="0 0 12 9"><path d="M1 8 Q2 3 8 3 V0 L12 4 L8 8 V5 Q4 5 1 8z" fill="#fff"/></svg><span>Reselling and supporting<br>Korvel Antivirus</span></a>
<a class="service-btn" style="top:992px;width:123px;height:25px"><svg width="12" height="9" viewBox="0 0 12 9"><path d="M1 8 Q2 3 8 3 V0 L12 4 L8 8 V5 Q4 5 1 8z" fill="#fff"/></svg>Tresby Apps</a>

<p class="service-copy">But I must explain to you how all this mistaken idea of denouncing pleasure and praising pain was born and I will give you a complete account of the system, and expound the actual teachings of the great explorer But I must explain to you how all this mistaken idea of denouncing pleasure and praising pain was born and I will give you a complete account of the system</p>
<span class="btn-more service-more">Learn More</span>

<footer class="site-footer"></footer>
<div class="footer-links" style="left:76px">Home<br>About<br>Services</div>
<div class="footer-links" style="left:126px">Products<br>Downloads<br>Contact</div>
<div class="call-label">call us</div>
<div class="call-number">(0100) 5550 1234</div>
<p class="footer-note">We already support hundreds of cafes and restaurants.<br>We are also about to launch and promote a range... <a>Learn More</a></p>
<div class="footer-rule"></div>
<p class="legal" style="top:1145px">All Right Reseved Copyright © 2012 - Privacy Policy | Terms of Use</p>
<p class="legal" style="top:1159px">Powered By : Northgrid Studio</p>

</body>
</html>
```